Building Maintenance Flyer specialising in hot and silent pressure cleaning

Hi. I love this flyer. I would like something similar but with hot water pressure washing and building maintenance

Ferro Lane & Services provides high pressure steam cleaning and water blasting services throughout Brisbane and surrounding areas, covering the Industrial, Commercial, Strata and Residential property owners sectors.

FLS combining the cleaning power of heat with state-of-the-art silent equipment, accredited technicians and a steadfast commitment to the environment. We offer the best Prompt, Professional Service.

Fully Accredited & Certified Technicians
100% Satisfaction Guaranteed
We are a family owned and operated business and love what we do. No job is too big or too small and we take pride in our work.
All of our services are undertaken using industry leading equipment and, providing safe and superior results.

Our business is covered by 20 million full public liability insurance and we operate within strict health & safety guidelines, providing all our clients with complete peace of mind. Project plans and risk assessments can also be provided upon request.

BODY CORPORATES

BUILDING FAÇADE CLEANING

CAR PARKS – underground, single and multi level

DRIVE THRU

FOOD PRODUCTION FACILITIES CLEANING SANITISING

SHOPPING CENTRES

BIRD MANAGEMENT AND DECONTAMINATION

GENERAL MAINTENANCE

CONSTRUCTION CLEAN UPS

SPILL MANAGEMENT

CONCRETE CLEANING AND DEGRASING

CONCRETE SEALING

FACTORY CLEANING & CLEAN UP

ENVIRONMENTAL DECONTAMINATION OF HEAVY VEHICLES AND EQUIPMENT

SITE CLEANS AND RUBBISH REMOVAL

MANUFACTURING PLANTS

Target Market(s)

Facility Managers, Commercial and Industrial Property Owners, Property Managers, Schools, Restaurants,

Industry/Entity Type

Pressure Cleaning

Font styles to use
Sans Serif

Colors
0293ce
00a990
33a6d7
33b8a4

Requirements
Must have
• SILENT HOT WATER PRESSURE CLEANING
Runs up to 120 Degrees Celsius
SANITISING - Bin areas, outdoor areas, cafe's, restaurants, schools, drive thru's
Blue's and Greens to link in with our logo

```html
<!DOCTYPE html>
<html lang="en">
<head>
<meta charset="utf-8">
<title>FLS Property Maintenance Flyer</title>
<link href="https://fonts.googleapis.com/css2?family=Montserrat:wght@500;600;700;800;900&family=Open+Sans:wght@400;600;700&display=swap" rel="stylesheet">
<style>
  :root{
    --page:#e9eef0;
    --blue:#2f5db2;
    --blue-deep:#244c9a;
    --sky:#0293ce;
    --teal:#5cbfb6;
    --teal-deep:#00a990;
    --ink:#1f2a36;
    --shadow:#2f3338;
    --white:#ffffff;
  }
  *{margin:0;padding:0;box-sizing:border-box}
  html,body{width:1200px;height:995px;overflow:hidden;background:var(--page)}
  body{position:relative;font-family:"Open Sans",sans-serif;color:var(--ink)}
  .flyer{position:absolute;left:40px;top:101px;width:1120px;height:792px;background:var(--white);overflow:hidden;box-shadow:0 10px 30px rgba(0,0,0,.18)}
  .flyer-shapes{position:absolute;inset:0}
  .abs{position:absolute}
  .brand{left:720px;top:40px;display:flex;align-items:center;gap:12px}
  .brand-dot{width:46px;height:46px;border-radius:50%;background:var(--blue)}
  .brand-name{font-family:"Montserrat",sans-serif;font-weight:800;font-size:40px;color:var(--blue);letter-spacing:1px}
  .headline{left:600px;top:118px;width:480px;text-align:center;font-family:"Montserrat",sans-serif}
  .headline .kicker{font-weight:700;font-size:22px;line-height:1.1;color:var(--blue);text-transform:uppercase}
  .headline .main{font-weight:900;font-size:50px;line-height:1.05;color:var(--teal);letter-spacing:1px}
  .headline .sub{font-weight:500;font-size:18px;line-height:1.2;color:var(--ink);margin-top:4px}
  .headline .sub b{font-weight:800}
  .features{left:600px;top:295px;width:280px;list-style:none}
  .features li{display:flex;gap:12px;align-items:flex-start;margin-bottom:12px;font-size:12.5px;line-height:1.25}
  .features .icon{flex:none;width:22px;height:22px}
  .features b{font-family:"Montserrat",sans-serif;font-weight:700;font-size:13px;text-transform:uppercase}
  .solutions{left:60px;top:520px;width:520px;color:var(--white)}
  .solutions h2{font-family:"Montserrat",sans-serif;font-weight:800;font-size:28px;margin-bottom:18px;margin-left:20px}
  .solution-grid{display:grid;grid-template-columns:1fr 1fr;column-gap:20px;row-gap:18px;list-style:none}
  .solution-grid li{display:flex;align-items:center;gap:12px;font-size:14px;line-height:1.2}
  .solution-grid .icon{flex:none;width:26px;height:26px}
  .contact{left:645px;top:585px;width:460px;color:var(--blue)}
  .phone{display:flex;align-items:center;gap:10px;font-family:"Montserrat",sans-serif;font-weight:800;font-size:34px;line-height:1.2;color:var(--blue-deep)}
  .contact-row{display:flex;align-items:center;gap:12px;margin-top:6px;font-size:15px}
  .contact-row.web{font-size:20px;font-weight:600}
  .contact-row .icon{flex:none;width:18px;height:18px}
  .contact-row.address{font-size:13px}
</style>
</head>
<body>
<main class="flyer">
  <svg class="flyer-shapes" viewBox="0 0 1120 792" width="1120" height="792">
    <defs>
      <linearGradient id="photoTone" x1="0" y1="0" x2="1" y2="1">
        <stop offset="0" stop-color="#8aa6b8"/>
        <stop offset=".45" stop-color="#4d5356"/>
        <stop offset="1" stop-color="#7c8b8e"/>
      </linearGradient>
      <linearGradient id="staffTone" x1="0" y1="0" x2="0" y2="1">
        <stop offset="0" stop-color="#3d8f87"/>
        <stop offset=".6" stop-color="#3a63b4"/>
        <stop offset="1" stop-color="#e5cf3a"/>
      </linearGradient>
    </defs>
    <rect role="img" aria-label="Photo of a technician pressure washing paving beside a stone brick wall" x="0" y="0" width="640" height="600" fill="url(#photoTone)"/>
    <path d="M548 0 C485 190 495 380 600 530 L640 792 H1120 V0 Z" fill="var(--teal)"/>
    <path d="M535 0 C470 190 485 370 588 528" fill="none" stroke="var(--shadow)" stroke-width="14"/>
    <path d="M582 0 H1120 V455 C960 505 790 520 620 495 C528 375 522 190 582 0 Z" fill="var(--white)"/>
    <path d="M630 792 C620 700 612 620 614 562 C780 578 960 548 1120 498 V792 Z" fill="var(--white)"/>
    <path d="M0 792 V470 C140 395 360 385 500 440 C590 480 620 620 640 792 Z" fill="var(--teal)"/>
    <path d="M0 792 V490 C140 420 350 410 480 455 C560 485 590 620 610 792 Z" fill="var(--blue)"/>
    <circle cx="505" cy="455" r="42" fill="var(--sky)" stroke="var(--white)" stroke-width="4"/>
    <rect role="img" aria-label="Photo of a smiling cleaner in green overalls with a mop and a yellow janitorial cart" x="895" y="290" width="210" height="320" rx="6" fill="url(#staffTone)" opacity=".85"/>
  </svg>

  <div class="abs brand">
    <span class="brand-dot"></span>
    <span class="brand-name">FLS</span>
  </div>

  <header class="abs headline">
    <p class="kicker">Allcommercial<br>&amp; Industrial Property</p>
    <p class="main">MAINTENANCE</p>
    <p class="sub"><b>FLS</b> - servicing Southeast's<br>Commercial &amp; Industrial sector 24/7</p>
  </header>

  <ul class="abs features">
    <li><svg class="icon" viewBox="0 0 22 22"><circle cx="11" cy="11" r="8" fill="none" stroke="var(--blue)" stroke-width="2"/><path d="M11 6v5l3 3" stroke="var(--blue)" stroke-width="2" fill="none"/></svg><b>We operate 24/7, 7 days a week</b></li>
    <li><svg class="icon" viewBox="0 0 22 22"><path d="M3 18h10M6 18V9h4v9M10 11l8-4" stroke="var(--blue)" stroke-width="2" fill="none"/></svg><span><b>Silent hot water pressure cleaning</b><br>Runs up to 120 degrees Celsius</span></li>
    <li><svg class="icon" viewBox="0 0 22 22"><circle cx="11" cy="11" r="5" fill="var(--blue)"/><path d="M11 2v4M11 16v4M2 11h4M16 11h4" stroke="var(--blue)" stroke-width="2"/></svg><b>COVID-19 Trained</b></li>
    <li><svg class="icon" viewBox="0 0 22 22"><path d="M4 16h14l-2-6H6z" fill="var(--blue)"/><circle cx="15" cy="5" r="2" fill="var(--sky)"/></svg><span><b>Sanitising</b> - Bin areas, Outdoor areas, Cafe's, Restaurants, Schools, Drive Thru's</span></li>
  </ul>

  <section class="abs solutions">
    <h2>Solutions For:</h2>
    <ul class="solution-grid">
      <li><svg class="icon" viewBox="0 0 26 26"><circle cx="13" cy="13" r="6" fill="var(--white)"/><path d="M13 2v5M13 19v5M2 13h5M19 13h5" stroke="var(--white)" stroke-width="2"/></svg>COVID-19<br>Infection Control</li>
      <li><svg class="icon" viewBox="0 0 26 26"><path d="M3 13L13 4l10 9M6 11v11h14V11" stroke="var(--white)" stroke-width="2" fill="none"/></svg>Common Area<br>Cleaning</li>
      <li><svg class="icon" viewBox="0 0 26 26"><path d="M4 22V10l9-6 9 6v12z" fill="var(--white)"/></svg>Building<br>Management</li>
      <li><svg class="icon" viewBox="0 0 26 26"><path d="M4 20c6-2 10-8 18-14-2 8-8 13-14 14z" fill="var(--white)"/></svg>Bird waste<br>removal</li>
      <li><svg class="icon" viewBox="0 0 26 26"><path d="M6 7h14l-2 16H8zM4 5h18" stroke="var(--white)" stroke-width="2" fill="none"/></svg>Bin Cleaning<br>&amp; Sanitation</li>
      <li><svg class="icon" viewBox="0 0 26 26"><path d="M3 18h20M6 18l3-8h8l3 8" stroke="var(--white)" stroke-width="2" fill="none"/></svg>Mould &amp; Mildew<br>removal</li>
      <li><svg class="icon" viewBox="0 0 26 26"><circle cx="9" cy="5" r="2.5" fill="var(--white)"/><path d="M9 9v7l-3 7M9 16l4 7M9 12l8 6" stroke="var(--white)" stroke-width="2" fill="none"/></svg>Garden<br>Maintenance</li>
      <li><svg class="icon" viewBox="0 0 26 26"><path d="M13 3c4 6 6 9 6 12a6 6 0 01-12 0c0-3 2-6 6-12z" fill="var(--white)"/></svg>Oil and Grease<br>elimination</li>
    </ul>
  </section>

  <section class="abs contact">
    <p class="phone"><svg width="28" height="28" viewBox="0 0 24 24"><path d="M6.6 10.8a15 15 0 006.6 6.6l2.2-2.2c.3-.3.7-.4 1-.2 1.1.4 2.3.6 3.6.6.6 0 1 .4 1 1V20c0 .6-.4 1-1 1A17 17 0 013 4c0-.6.4-1 1-1h3.5c.6 0 1 .4 1 1 0 1.3.2 2.5.6 3.6.1.3 0 .7-.2 1z" fill="var(--blue-deep)"/></svg>555-014-2830</p>
    <p class="contact-row web"><svg class="icon" viewBox="0 0 18 18"><circle cx="9" cy="9" r="7.5" fill="none" stroke="var(--blue)" stroke-width="1.6"/><path d="M1.5 9h15M9 1.5c3 3 3 12 0 15M9 1.5c-3 3-3 12 0 15" stroke="var(--blue)" stroke-width="1.2" fill="none"/></svg>www.ferrolane.example</p>
    <p class="contact-row"><svg class="icon" viewBox="0 0 18 18"><rect x="1" y="3.5" width="16" height="11" fill="var(--blue)"/><path d="M1 4l8 6 8-6" stroke="var(--white)" stroke-width="1.4" fill="none"/></svg>office@ferrolane.example</p>
    <p class="contact-row address"><svg class="icon" viewBox="0 0 18 18"><path d="M9 1a6 6 0 016 6c0 4-6 10-6 10S3 11 3 7a6 6 0 016-6z" fill="var(--blue)"/><circle cx="9" cy="7" r="2.2" fill="var(--white)"/></svg>48 Dunmore Street, Corvale California 90417</p>
  </section>
</main>
</body>
</html>
```